Zielgruppe
Tobias Fink Personal Training.
Personaltraining für Bürotätige / leitende Positionen.
Rücken- und Haltungstraining.
Zielgruppe: Herren mittleren Alters, gehobene Klasse.
Aufgabenstellung
Schlicht, elegant, hochwertig
Gerne Logo eingearbeitet.
Schwarz / Gold / Weiß

```html
<!DOCTYPE html>
<html lang="de">
<head>
<meta charset="utf-8">
<title>Tobias Fink Personal Training – Visitenkarten</title>
<link rel="stylesheet" href="https://fonts.googleapis.com/css2?family=Montserrat:wght@400;600;700;800&family=Roboto+Slab:wght@400;700&display=swap">
<style>
  :root {
    --bg: #dedede;
    --bg-top: #e4e4e4;
    --gold: #c1a23a;
    --gold-dark: #a8892a;
    --black: #1c1a19;
    --card-dark: #231e1c;
    --white: #ffffff;
    --ink: #2a2a2a;
  }
  * { margin: 0; padding: 0; box-sizing: border-box; }
  html, body { width: 1200px; height: 2307px; overflow: hidden; }
  body {
    position: relative;
    background: var(--bg);
    font-family: "Montserrat", sans-serif;
    color: var(--ink);
  }
  .stage-top {
    position: absolute; left: 0; top: 0; width: 1200px; height: 745px;
    background: var(--bg-top);
  }
  .card {
    position: absolute; width: 510px; height: 334px; overflow: hidden;
    box-shadow: 0 18px 40px rgba(0,0,0,0.16);
  }

  /* front: dark */
  .card-front { background: var(--card-dark); }
  .card-front .texture {
    position: absolute; inset: 0;
    background: linear-gradient(180deg, #2a2523 0%, #211c1a 55%, #1e1a18 100%);
  }
  .card-front .frame {
    position: absolute; left: 16px; top: 16px; right: 16px; bottom: 16px;
    border: 3px solid var(--gold);
  }
  .card-front .brand {
    position: absolute; left: 0; right: 0; top: 128px; text-align: center;
    font-family: "Montserrat", sans-serif; font-weight: 800;
    font-size: 78px; line-height: 1; letter-spacing: -2px; color: var(--gold);
  }

  /* back: white */
  .card-back { background: var(--white); }
  .card-back .holder {
    position: absolute; left: 52px; top: 46px;
    font-family: "Roboto Slab", serif; color: var(--gold); line-height: 26px;
  }
  .holder .name { font-weight: 700; font-size: 19px; }
  .holder .role { font-weight: 400; font-size: 19px; }
  .card-back .company {
    position: absolute; left: 52px; top: 160px; font-size: 14px; line-height: 21px;
  }
  .company .company-name { color: var(--gold); font-weight: 700; }
  .company .address { color: var(--ink); font-weight: 400; font-size: 14.5px; }
  .card-back .brand {
    position: absolute; left: 292px; top: 42px;
    font-family: "Montserrat", sans-serif; font-weight: 800;
    font-size: 66px; line-height: 1; letter-spacing: -2px; color: var(--gold);
  }
  .card-back .contact {
    position: absolute; left: 292px; top: 160px; list-style: none;
    font-size: 14.5px; line-height: 25px; color: var(--ink);
  }
  .contact li { display: flex; align-items: center; gap: 8px; height: 25px; }
  .contact svg { width: 15px; height: 15px; flex: none; }
  .card-back .rule-gold {
    position: absolute; top: 289px; height: 2px; background: var(--gold);
  }
  .card-back .rule-black {
    position: absolute; top: 295px; height: 7px; background: var(--black);
  }
  .rule-left { left: 0; width: 391px; }
  .rule-right { left: 466px; width: 44px; }
  .card-back .rule-mark {
    position: absolute; left: 416px; top: 283px; width: 26px; height: 26px;
    background: var(--gold);
  }

  .caption {
    position: absolute; left: 918px; top: 1926px;
    font-family: "Montserrat", sans-serif; font-weight: 800; font-size: 23px; line-height: 30px;
  }
  .caption .line-dark { color: var(--black); }
  .caption .line-gold { color: var(--gold); }
</style>
</head>
<body>

<div class="stage-top"></div>

<!-- pair overview -->
<article class="card card-back" style="left:60px; top:205px;">
  <div class="holder"><div class="name">Jonas Beispiel</div><div class="role">Geschäftsführer</div></div>
  <div class="brand">TFPT</div>
  <div class="company">
    <div class="company-name">Tobias Fink</div>
    <div class="company-name">Personal Training</div>
    <div class="address">Lindenweg 12</div>
    <div class="address">Musterstadt 10115</div>
  </div>
  <ul class="contact">
    <li><svg viewBox="0 0 16 16"><rect x="4" y="1" width="8" height="14" rx="1.5" fill="none" stroke="var(--gold)" stroke-width="1.4"/><circle cx="8" cy="12.5" r="0.9" fill="var(--gold)"/></svg>+41 22 480 15 30</li>
    <li><svg viewBox="0 0 16 16"><path d="M1 6 Q8 1 15 6 L13 8 L11 6.5 L5 6.5 L3 8 Z" fill="var(--gold)"/><rect x="3" y="8" width="10" height="6" rx="1" fill="var(--gold)"/></svg>+41 22 480 15 30</li>
    <li><svg viewBox="0 0 16 16"><rect x="1" y="3.5" width="14" height="9" rx="1" fill="var(--gold)"/><path d="M1.5 4 L8 9 L14.5 4" fill="none" stroke="#fff" stroke-width="1.2"/></svg>info@fink-training.de</li>
    <li><svg viewBox="0 0 16 16"><circle cx="8" cy="8" r="6.3" fill="none" stroke="var(--gold)" stroke-width="1.3"/><ellipse cx="8" cy="8" rx="2.8" ry="6.3" fill="none" stroke="var(--gold)" stroke-width="1.1"/><path d="M2 8 H14 M3 5 H13 M3 11 H13" stroke="var(--gold)" stroke-width="1"/></svg>www.fink-training.de</li>
  </ul>
  <div class="rule-gold rule-left"></div><div class="rule-black rule-left"></div>
  <div class="rule-mark"></div>
  <div class="rule-gold rule-right"></div><div class="rule-black rule-right"></div>
</article>

<article class="card card-front" style="left:630px; top:205px;">
  <div class="texture" role="img" aria-label="Dezentes dunkles Hintergrundmuster"></div>
  <div class="frame"></div>
  <div class="brand">TFPT</div>
</article>

<!-- front -->
<article class="card card-front" style="left:345px; top:870px;">
  <div class="texture" role="img" aria-label="Dezentes dunkles Hintergrundmuster"></div>
  <div class="frame"></div>
  <div class="brand">TFPT</div>
</article>

<!-- back -->
<article class="card card-back" style="left:345px; top:1326px;">
  <div class="holder"><div class="name">Jonas Beispiel</div><div class="role">Geschäftsführer</div></div>
  <div class="brand">TFPT</div>
  <div class="company">
    <div class="company-name">Tobias Fink</div>
    <div class="company-name">Personal Training</div>
    <div class="address">Lindenweg 12</div>
    <div class="address">Musterstadt 10115</div>
  </div>
  <ul class="contact">
    <li><svg viewBox="0 0 16 16"><rect x="4" y="1" width="8" height="14" rx="1.5" fill="none" stroke="var(--gold)" stroke-width="1.4"/><circle cx="8" cy="12.5" r="0.9" fill="var(--gold)"/></svg>+41 22 480 15 30</li>
    <li><svg viewBox="0 0 16 16"><path d="M1 6 Q8 1 15 6 L13 8 L11 6.5 L5 6.5 L3 8 Z" fill="var(--gold)"/><rect x="3" y="8" width="10" height="6" rx="1" fill="var(--gold)"/></svg>+41 22 480 15 30</li>
    <li><svg viewBox="0 0 16 16"><rect x="1" y="3.5" width="14" height="9" rx="1" fill="var(--gold)"/><path d="M1.5 4 L8 9 L14.5 4" fill="none" stroke="#fff" stroke-width="1.2"/></svg>info@fink-training.de</li>
    <li><svg viewBox="0 0 16 16"><circle cx="8" cy="8" r="6.3" fill="none" stroke="var(--gold)" stroke-width="1.3"/><ellipse cx="8" cy="8" rx="2.8" ry="6.3" fill="none" stroke="var(--gold)" stroke-width="1.1"/><path d="M2 8 H14 M3 5 H13 M3 11 H13" stroke="var(--gold)" stroke-width="1"/></svg>www.fink-training.de</li>
  </ul>
  <div class="rule-gold rule-left"></div><div class="rule-black rule-left"></div>
  <div class="rule-mark"></div>
  <div class="rule-gold rule-right"></div><div class="rule-black rule-right"></div>
</article>

<!-- alternative back -->
<article class="card card-back" style="left:345px; top:1782px;">
  <div class="holder"><div class="name">Jonas Beispiel</div><div class="role">Geschäftsführer</div></div>
  <div class="brand">TFPT</div>
  <div class="company">
    <div class="company-name">Tobias Fink</div>
    <div class="company-name">Personal Training</div>
    <div class="address">Lindenweg 12</div>
    <div class="address">Musterstadt 10115</div>
  </div>
  <ul class="contact">
    <li><svg viewBox="0 0 16 16"><rect x="4" y="1" width="8" height="14" rx="1.5" fill="none" stroke="var(--gold)" stroke-width="1.4"/><circle cx="8" cy="12.5" r="0.9" fill="var(--gold)"/></svg>+41 22 480 15 30</li>
    <li><svg viewBox="0 0 16 16"><path d="M1 6 Q8 1 15 6 L13 8 L11 6.5 L5 6.5 L3 8 Z" fill="var(--gold)"/><rect x="3" y="8" width="10" height="6" rx="1" fill="var(--gold)"/></svg>+41 22 480 15 30</li>
    <li><svg viewBox="0 0 16 16"><rect x="1" y="3.5" width="14" height="9" rx="1" fill="var(--gold)"/><path d="M1.5 4 L8 9 L14.5 4" fill="none" stroke="#fff" stroke-width="1.2"/></svg>info@fink-training.de</li>
    <li><svg viewBox="0 0 16 16"><circle cx="8" cy="8" r="6.3" fill="none" stroke="var(--gold)" stroke-width="1.3"/><ellipse cx="8" cy="8" rx="2.8" ry="6.3" fill="none" stroke="var(--gold)" stroke-width="1.1"/><path d="M2 8 H14 M3 5 H13 M3 11 H13" stroke="var(--gold)" stroke-width="1"/></svg>www.fink-training.de</li>
  </ul>
  <div class="rule-gold rule-left"></div><div class="rule-black rule-left"></div>
  <div class="rule-mark"></div>
  <div class="rule-gold rule-right"></div><div class="rule-black rule-right"></div>
</article>

<div class="caption">
  <div class="line-dark">Alternative Back</div>
  <div class="line-gold">Gold Gradation</div>
</div>

</body>
</html>
```